Basketball Training Facility Flyer Design

We need a killer flyer designed for our brand new state of the art basketball training facility here in Syracuse, Utah. This flyer will be distributed to coaches, parents and players in a large school district in Davis and Weber county, Utah. The purpose of the flyer is to announce the launch of the new facility and to encourage parents, coaches and players to come and try out the facility for a free initial session. We're offering a completely complimentary first training session to introduce customers to the facility at no cost.

We use technology and equipment that is typically found in PLQ-level training facilities and gymnasiums. Our website can be found here for some additional information - www.crestcourthoops.net. Customers can easily book and pay online through our website (the functionality will be done by the time we distribute the completed flyer).

The design needs to highlight the equipment we offer at the facility, because no other basketball training center has the same level of technology we do. We want the flyer to be clean and simple.

Please see must haves for specific details.

The size of the flyer we want to print is 5.75 inches by 9.5 inches.

Target Market(s)

Parents of basketball players of all skill levels age 8-18.

Industry/Entity Type

Training

Requirements
Must have
• Design must include this header: You want to dominate on the court. We have the formula to make that happen.

Design must include this sub header or highlight: Free Introductory Training Session!

The design must include our Logo

The design must include the photos attached of the Ravel, the Liftorra and the 37Twelve

Under the the photo of the Ravel 5200 (attached) please include this verbiage:
Game Shots in Game Spots at Game Speed

Under the photo of the Liftorra (see attached) please include this verbiage:
Improve Power, Agility and Speed like Never Before

Under the photo of the 37Twelve (attached) please include this verbiage:
Real Time Statistics to Improve Dribble Speed, Accuracy and Right / Left Comparison

Include this verbiage somewhere in the design: Technology Used by PLQ and the Best D-1 College Teams

The design must include a strong call to action: Call or Click Now to Schedule A Free Training Session!

The design must include our contact information in easy-to-read font and size (also specifically highlighting the website):

Schedule Online in Less Than 60 Seconds!
Call or Click
801-574-2918
www.crestcourthoops.net
Nice to have
• For examples of the type of design we like, please see the attached images labeled

Please use stock photos of your preference to go in the flyer (preferably images of youth basketball training or kids in basketball training)

We don't want the flyer to be too cluttered, so please use images at your discretion.

Thank you!

```html
<!DOCTYPE html>
<html lang="en">
<head>
<meta charset="utf-8">
<title>Crest Court Academy – Free Introductory Training Session</title>
<link rel="stylesheet" href="https://fonts.googleapis.com/css2?family=Arimo:wght@400;700&family=Archivo+Black&display=swap">
<style>
  :root {
    --ink: #050505;
    --ember: #b3200e;
    --gold: #ffe533;
    --white: #ffffff;
    --arc: #2c6cff;
    --court-orange: #d96a1e;
  }
  * { margin: 0; padding: 0; box-sizing: border-box; }
  html, body { width: 726px; height: 1200px; overflow: hidden; background: var(--ink); }
  .flyer {
    position: relative; width: 726px; height: 1200px; overflow: hidden;
    background: radial-gradient(ellipse 80% 45% at 50% 18%, var(--ember) 0%, #5a0c06 45%, var(--ink) 80%);
    font-family: "Arimo", Arial, sans-serif;
  }
  .hero-photo {
    position: absolute; left: 60px; top: 0; width: 600px; height: 600px;
    background: radial-gradient(ellipse 55% 60% at 55% 30%, #7a5444 0%, #4a2a22 45%, rgba(20,6,4,0) 80%);
    opacity: .85;
  }
  .arcs { position: absolute; left: 0; top: 0; }
  .headline { position: absolute; line-height: 1; color: var(--gold); font-weight: 700; text-shadow: 2px 2px 0 var(--ink), -1px -1px 0 var(--ink), 0 0 10px rgba(0,0,0,.8); white-space: nowrap; }
  .big { font-family: "Archivo Black", "Arial Black", sans-serif; font-weight: 400; }
  .lead-in { left: 123px; top: 113px; font-size: 36px; }
  .dominate { left: 72px; top: 140px; font-size: 118px; }
  .on-court { left: 210px; top: 252px; font-size: 30px; }
  .we-have { left: 398px; top: 290px; font-size: 26px; color: var(--white); }
  .formula { left: 396px; top: 307px; font-size: 62px; }
  .make-happen { left: 400px; top: 369px; font-size: 22px; color: var(--white); }
  .free { left: 416px; top: 394px; font-size: 100px; }
  .introductory { left: 421px; top: 493px; font-size: 32px; color: var(--white); }
  .training-session { left: 474px; top: 534px; font-size: 22px; color: var(--white); }

  .brand-mark { position: absolute; left: 80px; top: 300px; width: 262px; height: 262px; border-radius: 50%; background: var(--court-orange); border: 5px solid var(--white); display: flex; align-items: center; justify-content: center; text-align: center; }
  .brand-name { font-family: "Arimo", Arial, sans-serif; font-weight: 700; font-size: 28px; line-height: 1.15; color: var(--white); }

  .gear { position: absolute; top: 584px; }
  .gear-photo { width: 100%; border: 2px solid var(--white); }
  .gear-caption { margin-top: 10px; color: var(--white); font-weight: 700; font-size: 17px; line-height: 1.2; text-align: center; text-shadow: 1px 1px 2px var(--ink); }
  .gear--liftorra { left: 49px; width: 188px; }
  .gear--liftorra .gear-photo { height: 170px; background: linear-gradient(160deg, #f3f3f3, #b9c3d4); }
  .gear--ravel { left: 268px; width: 188px; }
  .gear--ravel .gear-photo { height: 262px; background: linear-gradient(180deg, #f7f7f7 0%, #e4e4e4 50%, #c8372c 100%); }
  .gear--stats { left: 486px; width: 200px; }
  .gear--stats .gear-photo { height: 170px; margin: 0 5px; width: 190px; background: radial-gradient(circle at 42% 55%, #b5561c 0%, #7a3210 35%, #f4f4f4 60%); }

  .tech-line { position: absolute; left: 0; width: 100%; top: 946px; line-height: 1; text-align: center; color: var(--gold); font-weight: 700; font-size: 19px; }
  .cta-item { position: absolute; left: 0; width: 100%; line-height: 1; text-align: center; color: var(--gold); font-weight: 700; text-shadow: 2px 2px 0 var(--ink); }
  .cta-title { top: 985px; font-size: 54px; }
  .cta-schedule { top: 1047px; font-size: 22px; }
  .cta-call { top: 1078px; font-size: 22px; }
  .cta-phone { top: 1112px; font-size: 22px; }
  .cta-web { top: 1141px; font-size: 30px; }
</style>
</head>
<body>
<main class="flyer">
  <div class="hero-photo" role="img" aria-label="Photo of a basketball player shouting with intensity, lit in red"></div>

  <svg class="arcs" width="726" height="1200" viewBox="0 0 726 1200" aria-hidden="true">
    <g fill="none" stroke="var(--arc)" stroke-opacity=".55">
      <path d="M-40 1120 Q 363 620 766 1120" stroke-width="3"/>
      <path d="M-60 940 Q 120 720 363 740" stroke-width="2"/>
      <path d="M786 940 Q 606 720 363 740" stroke-width="2"/>
      <circle cx="363" cy="1260" r="380" stroke-width="2"/>
    </g>
  </svg>

  <p class="headline lead-in">You Want To</p>
  <h1 class="headline big dominate">Dominate</h1>
  <p class="headline on-court">On The Court?</p>
  <p class="headline we-have">We Have The</p>
  <p class="headline big formula">Formula</p>
  <p class="headline make-happen">To Make That Happen</p>

  <div class="brand-mark"><span class="brand-name">CREST COURT<br>ACADEMY</span></div>

  <p class="headline big free">Free</p>
  <p class="headline introductory">Introductory</p>
  <p class="headline training-session">Training Session</p>

  <section class="gear gear--liftorra">
    <div class="gear-photo" role="img" aria-label="Photo of an athlete training on the Liftorra resistance platform"></div>
    <p class="gear-caption">Improve Power,<br>Agility and Speed<br>Like Never Before</p>
  </section>
  <section class="gear gear--ravel">
    <div class="gear-photo" role="img" aria-label="Photo of the Ravel 5200 shooting machine with net and hoop"></div>
    <p class="gear-caption">Game Shots<br>at Game Spots<br>at Game Speed</p>
  </section>
  <section class="gear gear--stats">
    <div class="gear-photo" role="img" aria-label="Photo of the 37Twelve smart basketball beside a phone showing stats"></div>
    <p class="gear-caption">Real Time Statistics<br>To Improve Dribble<br>Speed, Accuracy and<br>Right/Left Comparison</p>
  </section>

  <p class="tech-line">Technlogy used by the PLQ and the Best D1 College Teams</p>

  <section class="cta">
    <p class="cta-item cta-title">CALL or CLICK NOW!</p>
    <p class="cta-item cta-schedule">Schedule Online&nbsp; in Less Than 60 Seconds</p>
    <p class="cta-item cta-call">Call or Click</p>
    <p class="cta-item cta-phone">801-574-2918</p>
    <p class="cta-item cta-web">www.crestcourthoops.net</p>
  </section>
</main>
</body>
</html>
```